Stationery Design Project

I am looking for stationary design for an automotive collision repair company. This needs to work with my business cards just designed here. I've attached. I need 8.5 x 11 stationary and corissponding envelopes. a jot tab note pad also. Our companies focus is very high end customer service driven . Our customer base is 35-65 middle to high income. Please include company name, logo, address, phone number, web address. The business card is two greys with green and white writing. I invision a light grey background with a darker grey band on it that contains the logo.
Updates

I justĀ 

Why is no one touching this project

Target Market(s)

60%. Women 40% men. Age 35-60

Industry/Entity Type

Automotive

Requirements
Must have
• Tie in with business cards. So it needs grey tones with green and white logo. Name, address, phone and web address. Must have 8.5 x 11 paper and envelopes.
Nice to have
• Jot tab notes

```html
<!DOCTYPE html>
<html lang="en">
<head>
<meta charset="utf-8">
<title>PanelPerfect Letterhead</title>
<link rel="stylesheet" href="https://fonts.googleapis.com/css2?family=Roboto:wght@400;700&display=swap">
<style>
  :root {
    --backdrop: #e4e4e4;
    --paper: #f1f1f1;
    --band: #4a4a4a;
    --green: #7db529;
    --green-light: #b9d98a;
    --ink-light: #dcdcdc;
    --divider: #6a6a6a;
  }
  html, body {
    margin: 0;
    width: 1200px;
    height: 968px;
    overflow: hidden;
    background: var(--backdrop);
    font-family: "Roboto", Arial, sans-serif;
  }
  .letterhead {
    position: absolute;
    left: 252px;
    top: 34px;
    width: 696px;
    height: 900px;
    background: var(--paper);
    box-shadow: 0 2px 10px rgba(0,0,0,0.12);
    overflow: hidden;
  }
  .letterhead-bands {
    position: absolute;
    inset: 0;
  }
  .brand {
    position: absolute;
    left: 430px;
    top: 20px;
    width: 170px;
    text-align: center;
  }
  .brand-name {
    display: flex;
    justify-content: center;
    align-items: center;
    gap: 6px;
    color: var(--green);
    font-weight: 700;
    font-size: 24px;
    line-height: 30px;
  }
  .brand-mark {
    width: 9px;
    height: 9px;
    border-radius: 50%;
    background: var(--green);
  }
  .brand-tagline {
    margin-top: 1px;
    color: var(--ink-light);
    font-size: 7px;
    letter-spacing: 1.8px;
    text-transform: uppercase;
  }
  .contact {
    position: absolute;
    left: 60px;
    top: 834px;
    display: flex;
    color: var(--ink-light);
    font-size: 10px;
    line-height: 15px;
  }
  .contact-group {
    padding: 0 16px;
    border-left: 1px solid var(--divider);
  }
  .contact-group:first-child {
    padding-left: 0;
    border-left: none;
  }
  .contact-label {
    color: var(--green);
    margin-right: 6px;
  }
</style>
</head>
<body>
  <main class="letterhead">
    <svg class="letterhead-bands" width="696" height="900" viewBox="0 0 696 900" aria-hidden="true">
      <path d="M0,0 H696 V112 C620,108 560,100 480,92 C360,78 200,60 0,68 Z" fill="var(--band)"/>
      <path d="M0,72 C200,64 360,82 480,96 C560,104 620,112 696,116" fill="none" stroke="var(--green-light)" stroke-width="4"/>
      <path d="M0,68 C200,60 360,78 480,92 C560,100 620,108 696,112" fill="none" stroke="var(--green)" stroke-width="3"/>
      <path d="M0,796 C150,794 300,804 420,814 C540,824 620,808 696,796 V900 H0 Z" fill="var(--band)"/>
      <path d="M0,792 C150,790 300,800 420,810 C540,820 620,804 696,792" fill="none" stroke="var(--green-light)" stroke-width="4"/>
      <path d="M0,796 C150,794 300,804 420,814 C540,824 620,808 696,796" fill="none" stroke="var(--green)" stroke-width="3"/>
    </svg>

    <header class="brand">
      <div class="brand-name"><span class="brand-mark"></span>PanelPerfect</div>
      <div class="brand-tagline">Where care comes standard</div>
    </header>

    <footer class="contact">
      <div class="contact-group">
        88 Mender Lane<br>Bodyshop Bay 3120
      </div>
      <div class="contact-group">
        <span class="contact-label">t.</span>03 5550 1234<br>
        <span class="contact-label">f.</span>03 5550 4321
      </div>
      <div class="contact-group">
        www.panelperfectauto.com<br>sam@panelperfectauto.com
      </div>
    </footer>
  </main>
</body>
</html>
```